" Atendemos de maneira integrada em reabilitação ,tanto odontológica como neurológica. Somos terapia ocupacional, fonoaudiologia, neuropediatria e odontologia. Trabalhamos com técnicas de ponta e muito proximidade com nossos pacientes e suas famílias. "

```html
<!DOCTYPE html>
<html lang="pt-BR">
<head>
<meta charset="UTF-8">
<title>ALTIVARE – Cartão de Visita</title>
<link rel="stylesheet" href="https://fonts.googleapis.com/css2?family=Montserrat:wght@400;500;600;800&display=swap">
<style>
  :root{
    --page-bg:#e9ebee;
    --navy-deep:#0b3258;
    --navy:#114a7a;
    --teal:#2c9dc6;
    --teal-light:#54b8d8;
    --green:#8cc152;
    --ink:#1b4776;
    --text-grey:#555b63;
    --white:#ffffff;
  }
  *{margin:0;padding:0;box-sizing:border-box;}
  html,body{width:1200px;height:1200px;overflow:hidden;}
  body{
    background:var(--page-bg);
    font-family:"Montserrat",Arial,sans-serif;
    display:flex;flex-direction:column;align-items:center;justify-content:center;gap:60px;
  }
  .card{
    position:relative;width:880px;height:489px;border-radius:26px;overflow:hidden;
  }
  .card-waves{position:absolute;inset:0;width:100%;height:100%;}

  /* front */
  .card-front{background:linear-gradient(160deg,var(--navy) 0%,var(--navy-deep) 100%);}
  .front-brand{
    position:absolute;left:0;right:0;top:170px;text-align:center;color:var(--white);
  }
  .brand-mark{
    display:block;width:46px;height:46px;border-radius:50%;background:var(--green);margin:0 auto 18px;
  }
  .brand-name{font-weight:800;font-size:64px;letter-spacing:1px;line-height:1;}
  .brand-sub{font-weight:400;font-size:22px;margin-top:6px;letter-spacing:.3px;}

  /* back */
  .card-back{background:var(--white);}
  .back-brand{position:absolute;left:70px;top:80px;color:var(--ink);}
  .back-brand .brand-mark{width:28px;height:28px;margin:0 0 10px 70px;}
  .back-brand .brand-name{font-size:42px;}
  .back-brand .brand-sub{font-size:14px;margin-top:3px;color:var(--ink);}
  .person{position:absolute;right:110px;top:150px;text-align:right;}
  .person-name{color:var(--teal);font-size:22px;font-weight:500;letter-spacing:.5px;}
  .person-role{color:var(--text-grey);font-size:13px;letter-spacing:.5px;margin-top:2px;}
  .contacts{position:absolute;right:60px;top:215px;list-style:none;}
  .contacts li{
    display:flex;align-items:center;justify-content:flex-end;gap:16px;
    height:38px;font-size:18px;color:#222;
  }
  .contact-icon{width:24px;height:24px;flex:none;}
</style>
</head>
<body>

  <section class="card card-front">
    <svg class="card-waves" viewBox="0 0 880 489" preserveAspectRatio="none" aria-hidden="true">
      <path d="M0 418 Q440 392 880 410 L880 489 L0 489 Z" fill="var(--teal)"/>
      <path d="M0 400 Q440 378 880 396" fill="none" stroke="var(--green)" stroke-width="4"/>
      <path d="M0 409 Q440 386 880 403" fill="none" stroke="var(--white)" stroke-width="2" opacity=".8"/>
    </svg>
    <div class="front-brand">
      <span class="brand-mark"></span>
      <div class="brand-name">ALTIVARE</div>
      <div class="brand-sub">Paulo Resende &amp; Lívia Amaral</div>
    </div>
  </section>

  <section class="card card-back">
    <svg class="card-waves" viewBox="0 0 880 489" preserveAspectRatio="none" aria-hidden="true">
      <path d="M0 390 Q300 430 880 462 L880 489 L0 489 Z" fill="var(--teal)"/>
      <path d="M0 405 Q320 440 880 470 L880 489 L0 489 Z" fill="var(--teal-light)" opacity=".6"/>
      <path d="M0 372 Q300 414 880 446" fill="none" stroke="var(--green)" stroke-width="3"/>
    </svg>
    <div class="back-brand">
      <span class="brand-mark"></span>
      <div class="brand-name">ALTIVARE</div>
      <div class="brand-sub">Paulo Resende &amp; Lívia Amaral</div>
    </div>
    <div class="person">
      <div class="person-name">NOME SOBRENOME</div>
      <div class="person-role">CARGO/FUNÇÃO</div>
    </div>
    <ul class="contacts">
      <li>nome@empresa.com.br
        <svg class="contact-icon" viewBox="0 0 24 24" aria-hidden="true"><circle cx="12" cy="12" r="12" fill="var(--teal)"/><rect x="6" y="8" width="12" height="8" rx="1" fill="var(--white)"/><path d="M6 8 L12 13 L18 8" fill="none" stroke="var(--teal)" stroke-width="1.3"/></svg>
      </li>
      <li>99 9999-0000
        <svg class="contact-icon" viewBox="0 0 24 24" aria-hidden="true"><circle cx="12" cy="12" r="12" fill="var(--teal)"/><path d="M8 6 L10.5 6 L11.5 9 L10 10.5 Q11.5 13.5 13.5 14 L15 12.5 L18 13.5 L18 16 Q12 18 8 12 Q6.5 9 8 6 Z" fill="var(--white)"/></svg>
      </li>
      <li>99 99999-9999
        <svg class="contact-icon" viewBox="0 0 24 24" aria-hidden="true"><circle cx="12" cy="12" r="12" fill="var(--teal)"/><rect x="8.5" y="5" width="7" height="14" rx="1.5" fill="var(--white)"/><rect x="9.7" y="7" width="4.6" height="8.5" fill="var(--teal)"/></svg>
      </li>
      <li>Rua do Projeto, 999
        <svg class="contact-icon" viewBox="0 0 24 24" aria-hidden="true"><circle cx="12" cy="12" r="12" fill="var(--teal)"/><path d="M12 19 Q7 13 7 10 A5 5 0 0 1 17 10 Q17 13 12 19 Z" fill="var(--white)"/><circle cx="12" cy="10" r="1.8" fill="var(--teal)"/></svg>
      </li>
    </ul>
  </section>

</body>
</html>
```